ORLU VBS website - sleek, sophisticated, uplifting

ORLU Center for Regenerative Medicine is a cutting-edge medical clinic aimed at providing treatment for various chronic conditions and help people stave off the declines usually associated with aging. We utilize the latest technology in regenerative medicine to help people with autoimmune conditions, musculoskeletal problems and chronic pain, neurodegenerative conditions, male enhancement, facial rejuvenation and hair restoration, etc. We provide personalized medicine, through highly compassionate and competent doctors and staff.

please look at my current website which is not focused on regenerative medicine, but some contents can stay, as far as the philosophy of the treatment: www.pvmwellnesshub.example. But the reason I am changing the name of the clinic is because the focus of the medical practice is shifted entirely to "regenerative medicine" - using the body's own healing mechanism such as stem cells and growth factors...

Please DO NOT recycle old graphics and pictures. I want this site to be brand new, fresh and original.

Would like the website to be more sophisticated and nicer-looking than this website: www.brightquo.example

Target Market(s)

People who care a great deal about their health (above age 35), wants to prevent declines in their looks and health as they are getting older. Generally high income sector of the society that can afford self-pay (no insurance accepted) expensive stem cell treatment ranging from $4000 to $20,000.

Industry/Entity Type

Healthcare

Coding

Number of Pages Required

5+ page

Font styles to use
Sans Serif
Other font styles liked:
• Al Bayan, Avenir, Didot, Open Sans or Tsukushi A Round Gothic for central text, but may use Chalkboard for titles, or others as seen fit

Colors

Designer to choose colors to be used in the design.

Requirements
Must have
• Ultra modern look, very clean & sleek images and layout, portraying a sense of sophistication and confidence. Works beautifully well with existing logo. Give a sense that the clinic employs cutting-edge science, and provide highly competent & compassionate services.
• More sophisticated and nicer-looking than this website: www.brightquo.example
Nice to have
• many pages and links to science articles
Should not have
• fonts too playful or hard to read.

```html
<!DOCTYPE html>
<html lang="en">
<head>
<meta charset="utf-8">
<title>ORLU Center for Regenerative Medicine</title>
<link rel="stylesheet" href="https://fonts.googleapis.com/css2?family=Merriweather:wght@400;700;900&family=Open+Sans:wght@400;600;700&display=swap">
<style>
:root{
  --gold:#c9962b;
  --gold-light:#e2b445;
  --ink:#231f20;
  --text:#4a4a4a;
  --muted:#8a8a8a;
  --line:#d9d9d9;
  --paper:#ffffff;
  --mist:#f1f1f1;
  --map-tone:#e3e4e2;
  --heading:'Merriweather', Georgia, serif;
  --body:'Open Sans', Arial, sans-serif;
}
*{box-sizing:border-box;margin:0;padding:0}
html,body{width:1200px;height:3152px;overflow:hidden}
body{position:relative;background:var(--paper);font-family:var(--body);color:var(--text)}
.abs{position:absolute}
a{color:inherit;text-decoration:none}

/* hero */
.hero{left:0;top:0;width:1200px;height:560px;background:linear-gradient(180deg,#2a2a2a 0%,#4a4a4a 55%,#8a8a8a 100%)}
.nav{top:64px;display:flex;gap:34px;font-size:12px;font-weight:700;color:#fff;text-transform:uppercase}
.nav-left{left:248px}
.nav-right{left:762px}
.nav .active{color:var(--gold);position:relative}
.nav .active::after{content:"";position:absolute;left:50%;top:22px;margin-left:-5px;border:5px solid transparent;border-bottom-color:var(--gold)}
.brand{left:500px;top:30px;width:200px;text-align:center;color:var(--gold)}
.brand-name{font-family:var(--heading);font-weight:700;font-size:42px;letter-spacing:2px;line-height:1}
.brand-sub{font-family:var(--heading);font-size:8px;margin-top:6px;color:#fff}
.hero-title{left:0;width:1200px;top:272px;text-align:center;font-family:var(--heading);font-size:30px;color:#fff;letter-spacing:1px}
.hero-title span{color:var(--gold)}
.hero-text{left:330px;width:540px;top:320px;text-align:center;font-size:12px;line-height:1.75;color:#e5e5e5}
.dots{left:940px;top:284px;display:flex;flex-direction:column;gap:6px}
.dots i{display:block;width:10px;height:10px;border-radius:50%;border:1px solid #bbb}
.dots i.on{background:var(--gold-light);border-color:var(--gold-light)}
.video{left:294px;top:451px;width:613px;height:339px;background:radial-gradient(circle at 45% 50%,#d4527a 0%,#a8324f 45%,#5b1a2c 100%);box-shadow:0 14px 30px rgba(0,0,0,.25)}
.play{left:576px;top:602px;width:48px;height:34px;border-radius:8px;background:#e52d27}
.play::after{content:"";position:absolute;left:19px;top:10px;border-left:13px solid #fff;border-top:7px solid transparent;border-bottom:7px solid transparent}
.video-caption{left:330px;width:540px;top:810px;text-align:center;font-size:12px;line-height:1.7}
.video-caption b{color:var(--ink)}

/* services */
.services-bg{left:0;top:882px;width:1200px;height:680px;background:linear-gradient(180deg,#ececec 0%,#f7f7f7 40%,#f3f3f3 100%)}
.eyebrow{font-family:var(--heading);font-size:12px;color:var(--gold);text-transform:uppercase;letter-spacing:1px}
.section-title{font-family:var(--heading);font-weight:700;font-size:27px;color:var(--ink);text-transform:uppercase;letter-spacing:.5px}
.rule{width:60px;height:2px;background:var(--gold);margin:10px auto 0}
.services-head{left:0;width:1200px;top:930px;text-align:center}
.services-head p{font-size:12px;margin-top:16px}
.grid{left:248px;top:1060px;width:705px;display:grid;grid-template-columns:repeat(3,235px);grid-template-rows:177px 177px}
.svc{text-align:center;padding-top:18px;border-right:1px solid var(--line);border-bottom:1px solid var(--line)}
.svc:nth-child(3n){border-right:none}
.svc:nth-child(n+4){border-bottom:none}
.svc svg{width:64px;height:64px}
.svc h3{font-size:11px;font-weight:700;color:var(--ink);margin-top:8px}
.svc p{font-size:10.5px;line-height:1.6;margin:6px auto 0;width:180px}
.svc.featured{background:var(--ink);margin:4px;border:none}
.svc.featured h3,.svc.featured p{color:#fff}

/* about */
.band-gold{left:0;top:1585px;width:1200px;height:140px}
.about{left:250px;top:1464px;width:700px;height:275px;background:#fff;box-shadow:0 6px 24px rgba(0,0,0,.12);text-align:center;padding-top:34px}
.about p{font-size:10.5px;line-height:1.75;width:640px;margin:22px auto 0}
.about p b{color:var(--ink)}
.read-more{display:inline-flex;align-items:center;gap:8px;font-size:10px;font-weight:700;color:var(--gold);text-transform:uppercase}
.read-more::before{content:"";border-left:6px solid var(--gold);border-top:4px solid transparent;border-bottom:4px solid transparent}
.read-more::after{content:"";border-right:6px solid var(--gold);border-top:4px solid transparent;border-bottom:4px solid transparent}
.about .read-more{margin-top:28px}

/* blog */
.blog-bg{left:0;top:1712px;width:1200px;height:546px;background:linear-gradient(180deg,#dcdcdc 0%,#e9e9e9 50%,#e4e4e4 100%)}
.blog-head{left:248px;top:1810px;width:170px}
.blog-head .section-title{font-size:27px;margin-top:4px}
.blog-head .rule{margin:8px 0 0}
.blog-head p{font-size:11px;line-height:1.7;margin-top:22px}
.arrows{left:248px;top:1968px;display:flex;gap:4px}
.arrows i{border-top:10px solid transparent;border-bottom:10px solid transparent}
.arrows .prev{border-right:14px solid var(--gold)}
.arrows .next{border-left:14px solid #bfa46a}
.post{left:433px;top:1810px;width:457px;height:376px;background:#fff;box-shadow:0 6px 20px rgba(0,0,0,.1);overflow:hidden}
.post-photo{width:457px;height:195px;background:linear-gradient(135deg,#bfc7c9 0%,#e8e4de 50%,#9ea9ad 100%)}
.post-body{padding:20px 24px 0}
.post-title{font-family:var(--heading);font-size:10.5px;font-weight:700;color:var(--gold);white-space:nowrap;letter-spacing:-.2px}
.post-meta{font-size:9.5px;font-weight:600;color:var(--ink);margin-top:10px}
.post-meta span{margin:0 8px;color:var(--muted)}
.post-body p{font-size:10px;line-height:1.7;margin-top:12px}
.post-body .read-more{margin-top:16px}
.post-badge{left:890px;top:2005px;width:60px;height:60px;background:var(--gold);display:flex;align-items:center;justify-content:center}

/* map + contact */
.contact-bg{left:0;top:2258px;width:1200px;height:766px;background:linear-gradient(180deg,#eef0f1 0%,#f8f8f8 60%,#f4f4f4 100%)}
.map{left:250px;top:2306px;width:700px;height:279px;background:var(--map-tone)}
.info{left:250px;width:275px;height:100px;background:#fff;box-shadow:0 4px 16px rgba(0,0,0,.08);padding:22px 26px}
.info h4{font-size:11px;font-weight:700;color:var(--ink)}
.info p{font-size:11px;line-height:1.6;margin-top:10px}
.info-icon{left:512px;width:60px;height:60px;background:var(--gold);display:flex;align-items:center;justify-content:center}
.contact-head{left:615px;top:2632px;width:335px}
.contact-head h2{font-family:var(--heading);font-size:25px;font-weight:700;color:var(--ink)}
.contact-head p{font-size:11px;line-height:1.7;margin-top:10px}
.field{left:615px;width:335px;height:34px;background:#fff;box-shadow:0 2px 8px rgba(0,0,0,.08);font-size:9.5px;padding:10px 12px;color:var(--text)}
.field.message{height:101px}
.submit{left:615px;top:2966px}

/* footer */
.footer{left:0;top:3024px;width:1200px;height:128px;background:#fff}
.foot-nav{left:250px;top:3064px;display:flex;gap:22px;font-size:10px;font-weight:700;color:var(--ink);text-transform:uppercase}
.foot-nav .active{color:var(--gold)}
.copyright{left:250px;top:3098px;font-size:9.5px;color:var(--text)}
.socials{left:651px;top:3070px;display:flex;gap:14px}
.socials i{display:block;width:38px;height:38px;border-radius:50%;border:2px solid var(--gold)}
.foot-brand{left:850px;top:3060px;width:115px;text-align:center;color:var(--gold)}
.foot-brand .brand-name{font-size:34px}
.foot-brand .brand-sub{color:var(--ink);font-size:7px}
</style>
</head>
<body>

<!-- hero -->
<div class="abs hero" role="img" aria-label="Monochrome photograph of a scientist using a microscope in a laboratory"></div>
<svg class="abs" style="left:0;top:420px" width="1200" height="260" viewBox="0 0 1200 260">
  <polygon points="0,120 1200,0 1200,260 0,260" fill="#fff"/>
  <polygon points="0,120 520,68 0,245" fill="#c9962b"/>
  <polygon points="760,44 1200,0 1200,120 1050,125" fill="#c9962b"/>
</svg>
<svg class="abs" style="left:0;top:690px" width="1200" height="200"><defs><linearGradient id="fade" x1="0" y1="0" x2="0" y2="1"><stop offset="0" stop-color="#fff"/><stop offset="1" stop-color="#ececec"/></linearGradient></defs><rect width="1200" height="200" fill="url(#fade)"/></svg>

<nav class="abs nav nav-left"><a class="active" href="#">Home</a><a href="#">Video</a><a href="#">Services</a></nav>
<nav class="abs nav nav-right"><a href="#">About Us</a><a href="#">Blog</a><a href="#">Contact Us</a></nav>
<div class="abs brand"><div class="brand-name">ORLU</div><div class="brand-sub">Center for Regenerative Medicine</div></div>

<h1 class="abs hero-title">MULTI-FACETED <span>HEALTH</span></h1>
<p class="abs hero-text">Lorem Ipsum has been the industry's standard dummy text ever since the 1500s, when an unknown printer took a galley of type and scrambled it to make a type specimen book.</p>
<div class="abs dots"><i></i><i></i><i></i><i class="on"></i></div>

<div class="abs video" role="img" aria-label="Video still: medical illustration of a kidney with blood vessels"></div>
<div class="abs play" aria-label="Play video"></div>
<p class="abs video-caption"><b>Lorem Ipsum</b> has been the industry's standard dummy text ever since the when an unknown printer took a galley of type and scrambled it to make a type specimen book.</p>

<!-- services -->
<div class="abs services-bg" role="img" aria-label="Faint grey photograph of doctors at work"></div>
<header class="abs services-head">
  <div class="eyebrow">Services</div>
  <h2 class="section-title">Lorem Ipsum</h2>
  <div class="rule"></div>
  <p>Lorem Ipsum is simply dummy text of the printing and typesetting industry.</p>
</header>
<div class="abs grid">
  <div class="svc">
    <svg viewBox="0 0 64 64" fill="none" stroke="#c9962b" stroke-width="2"><rect x="8" y="26" width="30" height="26" rx="3"/><path d="M18 26v-6h10v6"/><path d="M23 33v12M17 39h12"/><path d="M44 40c-6-5-6-10-2-12 2-1 4 0 5 2 1-2 3-3 5-2 4 2 4 7-2 12l-3 3z"/></svg>
    <h3>Lorem Ipsum</h3><p>Lorem Ipsum is simply dummy text of the printing and typesetting industry.</p>
  </div>
  <div class="svc featured">
    <svg viewBox="0 0 64 64" fill="none" stroke="#c9962b" stroke-width="2"><rect x="20" y="6" width="24" height="8" rx="2"/><rect x="16" y="14" width="32" height="38" rx="4"/><path d="M22 34h20M24 28v12M40 28v12"/></svg>
    <h3>Lorem Ipsum</h3><p>Lorem Ipsum is simply dummy text of the printing and typesetting industry.</p>
  </div>
  <div class="svc">
    <svg viewBox="0 0 64 64" fill="none" stroke="#c9962b" stroke-width="2"><path d="M32 8v48"/><circle cx="32" cy="8" r="3"/><path d="M14 16c8 6 28 6 36 0M24 26c0 8 16 8 16 16s-16 8-16 8"/></svg>
    <h3>Lorem Ipsum</h3><p>Lorem Ipsum is simply dummy text of the printing and typesetting industry.</p>
  </div>
  <div class="svc">
    <svg viewBox="0 0 64 64" fill="none" stroke="#c9962b" stroke-width="2"><ellipse cx="32" cy="32" rx="24" ry="9"/><ellipse cx="32" cy="32" rx="24" ry="9" transform="rotate(60 32 32)"/><ellipse cx="32" cy="32" rx="24" ry="9" transform="rotate(-60 32 32)"/><circle cx="32" cy="32" r="4"/></svg>
    <h3>Lorem Ipsum</h3><p>Lorem Ipsum is simply dummy text of the printing and typesetting industry.</p>
  </div>
  <div class="svc">
    <svg viewBox="0 0 64 64" fill="none" stroke="#c9962b" stroke-width="2"><rect x="14" y="10" width="36" height="46" rx="3"/><rect x="24" y="6" width="16" height="8" rx="2"/><path d="M20 34h7l3-6 4 12 3-6h7"/></svg>
    <h3>Lorem Ipsum</h3><p>Lorem Ipsum is simply dummy text of the printing and typesetting industry.</p>
  </div>
  <div class="svc">
    <svg viewBox="0 0 64 64" fill="none" stroke="#c9962b" stroke-width="2"><path d="M26 8h12M28 8v16c-10 4-14 12-12 20 2 8 10 12 16 12s14-4 16-12c2-8-2-16-12-20V8"/><path d="M18 40h28"/></svg>
    <h3>Lorem Ipsum</h3><p>Lorem Ipsum is simply dummy text of the printing and typesetting industry.</p>
  </div>
</div>

<!-- about -->
<svg class="abs band-gold" viewBox="0 0 1200 140" role="img" aria-label="Golden image band with a DNA strand on the left and an orange cell on the right">
  <defs>
    <linearGradient id="goldBand" x1="0" y1="0" x2="1" y2="1"><stop offset="0" stop-color="#e2b445"/><stop offset="1" stop-color="#b07d18"/></linearGradient>
    <linearGradient id="orangeBand" x1="0" y1="0" x2="1" y2="0"><stop offset="0" stop-color="#f3a54a"/><stop offset="1" stop-color="#d9731a"/></linearGradient>
  </defs>
  <polygon points="0,0 260,40 260,122 0,122" fill="url(#goldBand)"/>
  <polygon points="720,122 1200,40 1200,127" fill="url(#orangeBand)"/>
</svg>
<div class="abs blog-bg" role="img" aria-label="Faint grey photograph of a medical consultation"></div>
<section class="abs about">
  <div class="eyebrow">About Us</div>
  <h2 class="section-title">Regenerative Medicine</h2>
  <div class="rule"></div>
  <p><b>Lorem Ipsum</b> is simply dummy text of the printing and typesetting industry. Lorem Ipsum has been the industry's standard dummy text ever since the 1500s, when an unknown printer took a galley of type and scrambled it to make a type specimen book. Lorem Ipsum is simply dummy text of the printing and typesetting industry. Lorem Ipsum has been the industry's standard dummy text ever since the 1500s, when an unknown printer took a galley of type and scrambled it to make a type specimen book.</p>
  <a class="read-more" href="#">Read More</a>
</section>

<!-- blog -->
<div class="abs blog-head">
  <div class="eyebrow">Blog</div>
  <h2 class="section-title">Medicine</h2>
  <div class="rule"></div>
  <p>Lorem Ipsum is simply dummy text of the printing and typesetting industry.</p>
</div>
<div class="abs arrows"><i class="prev"></i><i class="next"></i></div>
<article class="abs post">
  <div class="post-photo" role="img" aria-label="Photograph of a doctor's hands writing notes across a desk from a patient"></div>
  <div class="post-body">
    <h3 class="post-title">Lorem Ipsum is simply dummy text of the printing and typesetting.</h3>
    <div class="post-meta">Community<span>|</span>No Comments</div>
    <p>Lorem Ipsum has been the industry's standard dummy text ever since the 1500s, when an unknown printer took a galley of type and scrambled. Lorem Ipsum has been the industry's standard dummy text ever since the 1500s, when an unknown printer took a</p>
    <a class="read-more" href="#">Read More</a>
  </div>
</article>
<div class="abs post-badge"><svg width="32" height="32" viewBox="0 0 64 64" fill="none" stroke="#fff" stroke-width="3"><rect x="14" y="10" width="36" height="46" rx="3"/><rect x="24" y="6" width="16" height="8" rx="2"/><path d="M20 34h7l3-6 4 12 3-6h7"/></svg></div>

<!-- map + contact -->
<div class="abs contact-bg" role="img" aria-label="Faint photograph of a doctor with a stethoscope"></div>
<div class="abs map" role="img" aria-label="Interactive street map showing the clinic location"></div>

<div class="abs info" style="top:2642px"><h4>Work Hours</h4><p>Monday – Saturday : 08:00 - 17:30<br>Sunday off Work</p></div>
<div class="abs info-icon" style="top:2636px"><svg width="34" height="34" viewBox="0 0 34 34" fill="none" stroke="#fff" stroke-width="2"><circle cx="17" cy="17" r="14"/><path d="M17 8v9l6 4"/></svg></div>
<div class="abs info" style="top:2757px"><h4>Call Directly</h4><p>(+000) 0000 00 0000</p></div>
<div class="abs info-icon" style="top:2751px"><svg width="34" height="34" viewBox="0 0 34 34" fill="none" stroke="#fff" stroke-width="2"><path d="M8 4l6 6-3 4c2 4 5 7 9 9l4-3 6 6-4 4C15 30 4 19 4 8z"/></svg></div>
<div class="abs info" style="top:2873px"><h4>Email</h4><p>hello@orlu-clinic.example</p></div>
<div class="abs info-icon" style="top:2867px"><svg width="36" height="28" viewBox="0 0 36 28" fill="none" stroke="#fff" stroke-width="2"><rect x="2" y="2" width="32" height="24"/><path d="M2 2l16 14L34 2M2 26l12-12M34 26L22 14"/></svg></div>

<div class="abs contact-head"><h2>Contact Us</h2><p>Lorem Ipsum is simply dummy text of the printing and typesetting industry.</p></div>
<div class="abs field" style="top:2717px">Your Name</div>
<div class="abs field" style="top:2759px">Your Email</div>
<div class="abs field" style="top:2801px">Subject</div>
<div class="abs field message" style="top:2843px">Your Message</div>
<a class="abs read-more submit" href="#">Submit</a>

<!-- footer -->
<footer class="abs footer"></footer>
<nav class="abs foot-nav"><a class="active" href="#">Home</a><a href="#">Video</a><a href="#">Services</a><a href="#">About Us</a><a href="#">Blog</a><a href="#">Contact Us</a></nav>
<p class="abs copyright">Copyright © 2018 Veltrane. All rights reserved.</p>
<div class="abs socials" aria-label="Social links"><i></i><i></i><i></i></div>
<div class="abs foot-brand"><div class="brand-name">ORLU</div><div class="brand-sub">Center for Regenerative Medicine</div></div>

</body>
</html>
```